Real Estate Business Folders, Business Cards, Envelopes & Letterhead

Im looking for trendy, modern & professional design concepts for my business folder that will be used for real estate documents and property report presentations. I'm also looking for Business card designs, envelopes and letterhead with a similar theme. I have a logo already and I would like the logo colors to be incorporated in the design concepts.

Target Market(s)

Real Estate Investors, Banks, Financial Institutions

Industry/Entity Type

Real Estate

Colors
0455a3
959595
d3d3d3
848484

Requirements
Must have
• Trendy Modern, High Class look. Please include logo and colors and incorporate some silver or metallic.
• Business Address: 4127 Corvello Blvd ste 208-310
• N. Las Vegas, NV 89084
• Phone: 702-555-0187
• Fax : 702-555-0142
• Email: info@brookmerecastlesales.example
• Website: BrookmereCastleSales.example

```html
<!DOCTYPE html>
<html lang="en">
<head>
<meta charset="utf-8">
<title>Brookmere Castle Sales – Business Card</title>
<link rel="stylesheet" href="https://fonts.googleapis.com/css2?family=Lato:wght@400;700&family=Oswald:wght@600&display=swap">
<style>
  :root {
    --page-bg: #161616;
    --card-bg: #1f1f1f;
    --card-edge: #2a2a2a;
    --silver: #d3d3d3;
    --silver-mid: #959595;
    --silver-dark: #848484;
    --emboss: #151515;
    --emboss-light: #2e2e2e;
  }
  * { margin: 0; padding: 0; box-sizing: border-box; }
  html, body { width: 1200px; height: 900px; overflow: hidden; background: var(--page-bg); }
  .canvas {
    width: 1200px; height: 900px;
    display: flex; flex-direction: column; align-items: center; justify-content: center;
    gap: 40px;
  }
  .card {
    width: 640px; height: 366px;
    background: radial-gradient(ellipse at 70% 40%, #262626 0%, var(--card-bg) 70%);
    border: 1px solid var(--card-edge);
    box-shadow: 0 16px 40px rgba(0,0,0,0.6);
    position: relative;
  }
  /* front */
  .card-front { display: flex; align-items: center; justify-content: center; }
  .brand { display: flex; align-items: center; gap: 14px; }
  .brand-mark { width: 18px; height: 18px; background: var(--silver); }
  .brand-name {
    font-family: "Lato", sans-serif; font-weight: 700;
    font-size: 34px; letter-spacing: 3px; text-transform: uppercase;
    color: var(--silver);
  }
  /* back */
  .card-back { font-family: "Lato", sans-serif; }
  .identity { position: absolute; left: 92px; top: 128px; width: 170px; text-align: right; }
  .person-name {
    font-family: "Oswald", sans-serif; font-weight: 600;
    font-size: 32px; line-height: 1; text-transform: uppercase; letter-spacing: 0.5px;
    color: var(--emboss);
    text-shadow: 0 1px 0 var(--emboss-light), 0 -1px 0 #0b0b0b;
  }
  .person-title { font-size: 15px; color: #3a3a3a; margin-top: 6px; }
  .divider { position: absolute; left: 285px; top: 118px; width: 1px; height: 96px; background: #3d3d3d; }
  .contact-list { position: absolute; left: 305px; top: 118px; list-style: none; }
  .contact-item { display: flex; align-items: center; gap: 10px; font-size: 15.5px; line-height: 24px; color: var(--silver); }
  .contact-item svg { width: 13px; height: 13px; flex: none; }
  .contact-item.extra { padding-left: 23px; }
  .address {
    position: absolute; left: 92px; bottom: 44px;
    font-size: 16px; color: var(--emboss);
    text-shadow: 0 1px 0 var(--emboss-light);
  }
</style>
</head>
<body>
<main class="canvas">
  <section class="card card-front" aria-label="Card front">
    <div class="brand">
      <span class="brand-mark"></span>
      <span class="brand-name">Brookmere Castle Sales</span>
    </div>
  </section>

  <section class="card card-back" aria-label="Card back">
    <div class="identity">
      <p class="person-name">Daniel Harlow</p>
      <p class="person-title">Director</p>
    </div>
    <div class="divider"></div>
    <ul class="contact-list">
      <li class="contact-item">
        <svg viewBox="0 0 16 16" fill="none" stroke="#959595" stroke-width="1.6"><path d="M4 1.5 L6 5 L4.5 6.5 Q6 10 9.5 11.5 L11 10 L14.5 12 L13 14.5 Q6 14 1.5 3 Z"/></svg>
        702-555-0187
      </li>
      <li class="contact-item">
        <svg viewBox="0 0 16 16" fill="#959595"><rect x="4" y="1.5" width="8" height="4"/><rect x="1.5" y="6" width="13" height="6" rx="1"/><rect x="4" y="11" width="8" height="3.5"/></svg>
        702-555-0142
      </li>
      <li class="contact-item">
        <svg viewBox="0 0 16 16" fill="none" stroke="#959595" stroke-width="1.4"><rect x="1.5" y="3.5" width="13" height="9"/><path d="M1.5 3.5 L8 9 L14.5 3.5"/></svg>
        info@brookmerecastlesales.example
      </li>
      <li class="contact-item">
        <svg viewBox="0 0 16 16" fill="none" stroke="#959595" stroke-width="1.3"><circle cx="8" cy="8" r="6.5"/><ellipse cx="8" cy="8" rx="3" ry="6.5"/><path d="M1.5 8 H14.5"/></svg>
        www.brookmerecastlesales.example
      </li>
      <li class="contact-item extra">www.BrookmereCastleSales.example</li>
    </ul>
    <p class="address">4127 Corvello Blvd ste 208-310 N. Las Vegas, NV 89084</p>
  </section>
</main>
</body>
</html>
```